plovu business card design

plovu is an incubator within RTM Media focused on unlocking the potential in underserved niche micro-verticals on the web. our mission is to rapidly develop and foster emerging micro-verticals bc they are ripe for growth - building interesting and trusted content experiences with unqiue, useful and cutting-edge delivery methods.please do all copy (except for RTM Media, which must look as typed here and in logo) in all lowercase. Also please use spaces between phone # extensions not dashes or periods. I have attached all variations of the logo.
Industry/Entity Type
Business
Contact Information for Business Card
daria feltow, ceo www.plovu.io 218 holbrook lane 3rd floor oakland ca 94731 415 602 0002m 510 985 7966d daria.feltow@plovu.io
Look and feel
Each slider illustrates characteristics of the customer's brand and the style your logo design should communicate.

```html
<!DOCTYPE html>
<html lang="en">
<head>
<meta charset="utf-8">
<title>plovu business card</title>
<link rel="stylesheet" href="https://fonts.googleapis.com/css2?family=Montserrat:wght@400;500;600&display=swap">
<style>
  :root {
    --backdrop: #3b3431;
    --card: #1b1b1c;
    --card-edge: #262627;
    --ink-white: #f2f2f2;
    --ink-soft: #d9d9d9;
    --ink-grey: #8c8c8c;
    --accent: #1a8f8f;
    --divider: #9a9a9a;
  }
  * { margin: 0; padding: 0; box-sizing: border-box; }
  html, body {
    width: 1200px; height: 787px; overflow: hidden;
    background: var(--backdrop);
    font-family: "Montserrat", Arial, sans-serif;
  }
  .stage {
    position: relative; width: 1200px; height: 787px;
  }
  .card {
    position: absolute; top: 239px;
    width: 540px; height: 309px;
    background: var(--card);
    border: 1px solid var(--card-edge);
    border-radius: 3px;
    box-shadow: 0 10px 30px rgba(0,0,0,0.35);
  }
  .card--back { left: 40px; }
  .card--front { left: 620px; }

  /* back side */
  .back-mark {
    position: absolute; left: 70px; top: 96px;
    display: flex; align-items: center; gap: 14px;
  }
  .back-wordmark {
    font-size: 56px; font-weight: 600; color: var(--ink-grey);
    letter-spacing: 1px; line-height: 1;
  }
  .back-dot {
    width: 22px; height: 22px; border-radius: 50%;
    background: var(--ink-grey);
  }
  .back-web {
    position: absolute; left: 72px; top: 200px;
    font-size: 12px; color: var(--ink-grey);
    letter-spacing: 6px;
  }

  /* front side */
  .brand {
    position: absolute; left: 200px; top: 44px;
  }
  .brand-row { display: flex; align-items: center; gap: 12px; }
  .brand-wordmark {
    font-size: 74px; font-weight: 600; color: var(--ink-white);
    line-height: 1; letter-spacing: 1px;
  }
  .brand-dot {
    width: 26px; height: 26px; border-radius: 50%;
    background: var(--accent); margin-top: 24px;
  }
  .brand-tagline {
    font-size: 13px; font-weight: 500; color: var(--ink-soft);
    margin-top: 4px; margin-left: 2px;
  }
  .person {
    position: absolute; right: 290px; top: 160px;
    text-align: right;
  }
  .person-name {
    font-size: 17px; font-weight: 500; color: var(--accent);
    margin-bottom: 6px;
  }
  .person-line {
    font-size: 14px; color: var(--ink-soft); line-height: 22px;
  }
  .divider {
    position: absolute; left: 268px; top: 166px;
    width: 1px; height: 108px; background: var(--divider);
  }
  .contacts {
    position: absolute; left: 286px; top: 172px;
    list-style: none;
  }
  .contact {
    display: flex; align-items: center; gap: 10px;
    font-size: 14px; color: var(--ink-soft); height: 24px;
  }
  .contact svg { width: 14px; height: 14px; fill: var(--accent); flex: none; }
</style>
</head>
<body>
<main class="stage">

  <section class="card card--back" aria-label="business card back">
    <div class="back-mark">
      <span class="back-wordmark">plovu</span>
      <span class="back-dot"></span>
    </div>
    <p class="back-web">www.plovu.co</p>
  </section>

  <section class="card card--front" aria-label="business card front">
    <div class="brand">
      <div class="brand-row">
        <span class="brand-wordmark">plovu</span>
        <span class="brand-dot"></span>
      </div>
      <p class="brand-tagline">an RTM Media incubator</p>
    </div>

    <div class="person">
      <p class="person-name">Daria Feltow</p>
      <p class="person-line">ceo</p>
      <p class="person-line">218 holbrook lane 3rd floor</p>
      <p class="person-line">oakland ca 94731</p>
    </div>

    <div class="divider"></div>

    <ul class="contacts">
      <li class="contact">
        <svg viewBox="0 0 16 16" aria-hidden="true"><path d="M3 1h3l1.5 4-2 1.3a9 9 0 0 0 4.2 4.2L11 8.5l4 1.5v3a2 2 0 0 1-2 2A12 12 0 0 1 1 3a2 2 0 0 1 2-2z"/></svg>
        <span>415 738 4196</span>
      </li>
      <li class="contact">
        <svg viewBox="0 0 16 16" aria-hidden="true"><path d="M4.5 0h7A1.5 1.5 0 0 1 13 1.5v13a1.5 1.5 0 0 1-1.5 1.5h-7A1.5 1.5 0 0 1 3 14.5v-13A1.5 1.5 0 0 1 4.5 0zM5 2v10h6V2zm3 11a1 1 0 1 0 0 2 1 1 0 0 0 0-2z"/></svg>
        <span>510 247 3859</span>
      </li>
      <li class="contact">
        <svg viewBox="0 0 16 16" aria-hidden="true"><path d="M0 3h16v1.2L8 9 0 4.2zM0 5.8l8 4.8 8-4.8V13H0z"/></svg>
        <span>daria.feltow@plovu.io</span>
      </li>
      <li class="contact">
        <svg viewBox="0 0 16 16" aria-hidden="true"><path d="M8 0a8 8 0 1 0 0 16A8 8 0 0 0 8 0zm0 3a2 2 0 1 1 0 4 2 2 0 0 1 0-4zm-4 9c.5-2 2-3 4-3s3.5 1 4 3z"/></svg>
        <span>www.plovu.co</span>
      </li>
    </ul>
  </section>

</main>
</body>
</html>
```